Seven nights at the harbour

Creation of the cover for the book: "Sept nuits sur le quai du port" with the joined photo of a 70 years old lady.
Title: "Seven nights along the old harbour"
Author: "Mireille Vaston"
Publisher: "Editions Morvane" (should be at the bottom of the page)
Format: 14 x 20.5 cm
The story: A senior lady (70 years old), divorced, with a beautiful face, still wants to seduce, even young men.
We found the perfect photo for the woman. We would like to ask you to make a modern cover from it.
Besoin de quelques jours pour choisir un design
Target Market(s)
Novels reader (adults)
Industry/Entity Type
book

```html
<!DOCTYPE html>
<html lang="fr">
<head>
<meta charset="utf-8">
<title>Sept nuits sur le quai du port — couverture</title>
<link rel="stylesheet" href="https://fonts.googleapis.com/css2?family=Barlow+Condensed:wght@600;700&family=Dancing+Script:wght@700&family=Courier+Prime&family=Open+Sans:wght@300&display=swap">
<style>
  :root{
    --plum:#6e1a66;
    --plum-deep:#4a1746;
    --violet:#9a4a9a;
    --lilac:#b8a3c4;
    --silver:#ecebf0;
    --pink:#e4207c;
    --white:#ffffff;
    --paper:#fbf3fb;
  }
  html,body{margin:0;padding:0;overflow:hidden;background:var(--plum-deep);}
  .cover{position:relative;width:1200px;height:821px;overflow:hidden;}
  .cover-photo{position:absolute;inset:0;
    background:
      radial-gradient(ellipse 300px 360px at 930px 420px, #cdbfcf 0%, #b59fbd 40%, transparent 75%),
      radial-gradient(ellipse 380px 420px at 240px 380px, #5d4d66 0%, #4a3552 55%, transparent 90%),
      linear-gradient(100deg, #5a2a5a 0%, #4b2c53 35%, #6b3570 50%, #9a7aa6 62%, #a58aae 80%, #86267f 100%);}
  .cover-photo--back{position:absolute;left:0;top:0;width:555px;height:821px;
    background:linear-gradient(180deg, rgba(90,30,90,.15), rgba(60,20,60,.45));}

  .title-block{position:absolute;color:var(--white);}
  .title-main{font-family:"Barlow Condensed",sans-serif;font-weight:700;text-transform:uppercase;letter-spacing:-1px;line-height:.85;margin:0;white-space:nowrap;}
  .title-sub{font-family:"Dancing Script",cursive;font-weight:700;color:var(--pink);line-height:1;word-spacing:-.2em;white-space:nowrap;}

  .back-title{left:156px;top:252px;width:250px;text-align:center;}
  .back-title .title-main{font-size:64px;}
  .back-title .title-sub{font-size:33px;margin-top:-8px;}

  .blurb{position:absolute;left:98px;top:392px;margin:0;font-family:"Courier Prime",monospace;font-size:17.5px;color:var(--white);line-height:40.4px;white-space:pre;}

  .spine-title{position:absolute;left:590px;top:168px;writing-mode:vertical-rl;}
  .spine-title .title-main{font-size:60px;color:var(--white);}
  .spine-sub{position:absolute;left:562px;top:168px;writing-mode:vertical-rl;font-size:30px;}
  .spine-author{position:absolute;left:584px;top:536px;writing-mode:vertical-rl;font-family:"Barlow Condensed",sans-serif;font-weight:700;font-size:23px;color:var(--white);text-transform:uppercase;letter-spacing:-.3px;white-space:nowrap;}

  .front-title{left:668px;top:160px;width:500px;}
  .front-title .title-main{font-size:128px;color:var(--silver);text-shadow:0 2px 6px rgba(80,40,90,.35);}
  .front-title .title-sub{font-size:62px;margin-top:-22px;margin-left:4px;}

  .author-box{position:absolute;left:561px;top:741px;width:359px;height:80px;background:var(--paper);}
  .author-name{position:absolute;right:27px;top:13px;margin:0;font-family:"Barlow Condensed",sans-serif;font-weight:700;font-size:46px;color:var(--violet);text-transform:uppercase;letter-spacing:-.5px;line-height:1;}
  .publisher{position:absolute;right:40px;top:756px;margin:0;font-family:"Open Sans",sans-serif;font-weight:300;font-size:30px;color:var(--white);line-height:1;}
</style>
</head>
<body>
<main class="cover">
  <div class="cover-photo" role="img" aria-label="Portrait photo of a woman with silver-lilac hair blowing across her face, purple tones"></div>
  <div class="cover-photo--back"></div>

  <section class="back">
    <div class="title-block back-title">
      <h2 class="title-main">Sept nuits</h2>
      <div class="title-sub">sur le quai du port</div>
    </div>
    <p class="blurb">Lorem Ipsum Lorem Ipsum Lorem Ipsum
Lorem Ipsum Lorem Ipsum Lorem Ipsum
Lorem Ipsum Lorem Ipsum Lorem Ipsum
Lorem Ipsum Lorem Ipsum Lorem Ipsum
Lorem Ipsum Lorem Ipsum Lorem Ipsum
Lorem Ipsum Lorem Ipsum Lorem Ipsum
Lorem Ipsum Lorem Ipsum Lorem Ipsum</p>
  </section>

  <section class="spine">
    <div class="spine-title"><span class="title-main">Sept nuits</span></div>
    <div class="title-sub spine-sub">sur le quai du port</div>
    <div class="spine-author">Mireille Vaston</div>
  </section>

  <section class="front">
    <div class="title-block front-title">
      <h1 class="title-main">Sept nuits</h1>
      <div class="title-sub">sur le quai du port</div>
    </div>
    <div class="author-box"><p class="author-name">Mireille Vaston</p></div>
    <p class="publisher">Editions Morvane</p>
  </section>
</main>
</body>
</html>
```